Rising Paths Web Design

I am starting a new company that will provide LIFE COACHING services - I have tried to design a website, but it's too complicated. Right now, it's just me - I'm the only person that will provide services through the website - I have used artmarket to purchase a logo (see below). I want to be able to update the website myself, but need a template - basic design. Because I am not technologically savvy enough to explain in words - I basically want to have a website that will provide basic information about my services (coaching), a page about me and my background, hopefully scheduling possibilities, and testimonials — also a page for writing/blogs. I bought a website through NetHarbor - so when I have a template, I guess I”d use that - but maybe I’ll need to work with a designer to actually get it up on the internet. I have a head shot that I’ll upload, too.
Target Market(s)
Clients from the independent (private school) world - teachers, administrators
Number of Pages Required
4 page
Look and feel
Each slider illustrates characteristics of the customer's brand and the style your logo design should communicate.

```html
<!DOCTYPE html>
<html lang="en">
<head>
<meta charset="utf-8">
<title>Rising Paths Coaching</title>
<link rel="stylesheet" href="https://fonts.googleapis.com/css2?family=Libre+Baskerville:wght@400;700&family=Poppins:wght@400;500;600;700&display=swap">
<style>
:root{
  --teal:#0aa595;
  --mint:#e9f8f5;
  --ink:#333333;
  --text:#555555;
  --footer:#3a3a3c;
  --white:#ffffff;
  --badge-bg:#f1f3f4;
}
*{margin:0;padding:0;box-sizing:border-box}
html,body{width:1200px;height:3650px;overflow:hidden;background:var(--white)}
body{position:relative;font-family:'Poppins',sans-serif;color:var(--text)}
.abs{position:absolute}
.serif{font-family:'Libre Baskerville',serif;color:var(--ink);font-weight:400;line-height:1}

.hero-bg{left:0;top:0;width:1200px;height:633px;background:var(--mint)}
.logo{left:94px;top:60px;font-family:'Libre Baskerville',serif;color:#2f4f4f;line-height:1}
.logo-name{font-size:15px;white-space:nowrap}
.logo-sub{margin-top:6px;margin-left:26px;font-size:9px;letter-spacing:2px}

.nav{top:58px;left:683px;display:flex;gap:30px;font-size:13.5px;font-weight:500;color:#333}
.nav .active{color:var(--teal);font-weight:600}
.nav-mark{left:672px;top:0;width:61px;height:3px;background:var(--teal)}

.hero-title{left:119px;top:200px;font-size:70px;line-height:68px}
.hero-text{left:120px;top:420px;width:430px;font-size:14.5px;line-height:23px}
.btn{display:flex;align-items:center;justify-content:center;font-weight:600;font-size:13px;text-transform:uppercase}
.hero-btn{left:122px;top:485px;width:162px;height:45px;background:var(--teal);color:var(--white)}
.hero-photo{left:631px;top:150px;width:447px;height:580px;background:linear-gradient(160deg,#b9b2a4,#e8e4dc 45%,#8a7d6a);box-shadow:0 30px 50px rgba(0,0,0,.18)}
.hero-leaf{left:1078px;top:298px;width:122px;height:156px;background:linear-gradient(135deg,#bfe9e2,#0aa595);opacity:.5}

.about-rule{left:326px;top:701px;width:1px;height:187px;background:#d8d8d8}
.about-title{left:222px;top:914px;font-size:60px;line-height:62px}
.about-text{left:506px;top:865px;width:470px;font-size:13.5px;line-height:25px}
.link{font-size:13px;font-weight:600;color:var(--teal);text-transform:uppercase;border-bottom:1px solid var(--teal);padding-bottom:1px}
.about-link{left:508px;top:1069px}

.services-card{left:537px;top:1228px;width:565px;height:541px;background:var(--white);box-shadow:0 10px 50px rgba(0,0,0,.08)}
.services-photo{left:98px;top:1169px;width:496px;height:489px;background:linear-gradient(170deg,#8f9aa3,#a9a49a 40%,#4a3c32);box-shadow:0 30px 50px rgba(0,0,0,.2)}
.services-title{left:662px;top:1305px;font-size:52px;line-height:53px}
.services-text{left:662px;top:1481px;width:390px;font-size:13.5px;line-height:23px}
.services-link{left:662px;top:1683px}

.blogs-band{left:0;top:2195px;width:1200px;height:350px;background:linear-gradient(var(--mint),var(--white))}
.section-title{width:1200px;left:0;text-align:center;font-size:50px}
.blogs-title{top:1872px}
.blog{top:1957px;width:275px;height:402px;background:var(--white);box-shadow:0 6px 30px rgba(0,0,0,.05)}
.blog-img{width:275px;height:238px}
.blog-body{padding:18px 23px}
.blog-date{font-size:11px;color:#999;font-weight:500}
.blog-head{margin-top:8px;font-size:18px;font-weight:600;color:#333}
.blog-text{margin-top:8px;font-size:13px;line-height:19px;color:#666}

.testi-title{top:2464px}
.testi{top:2543px;height:217px;background:var(--white);box-shadow:0 6px 30px rgba(0,0,0,.06);overflow:hidden}
.quote-mark{font-family:'Libre Baskerville',serif;font-size:120px;color:#ececec;line-height:1}
.avatar{width:88px;height:88px;border-radius:50%;background:linear-gradient(#d9d6d2,#8d8a86)}
.testi-text{font-size:13px;line-height:22px;color:#666}
.testi-name{font-size:14px;font-weight:600;color:#333;white-space:nowrap}
.testi-name span{font-size:10.5px;font-weight:400;color:#777;margin-left:6px}
.testi-co{font-size:10.5px;color:#777;white-space:nowrap}

.badge{top:2853px;width:176px;height:176px;border-radius:50%;background:var(--badge-bg)}
.badge-shape{position:absolute;left:50%;top:50%;transform:translate(-50%,-50%)}

.footer{left:0;top:3218px;width:1200px;height:432px;background:var(--footer)}
.cta{left:159px;top:3123px;width:884px;height:188px;background:var(--teal)}
.cta-title{left:73px;top:52px;font-family:'Libre Baskerville',serif;font-weight:700;font-size:40px;line-height:46px;color:var(--white)}
.cta-btn{left:646px;top:72px;width:163px;height:45px;background:var(--white);color:#222}
.flogo{left:100px;top:3440px;font-family:'Libre Baskerville',serif;color:var(--white);line-height:1}
.flogo-name{font-size:23px;white-space:nowrap}
.flogo-sub{margin-top:8px;margin-left:33px;font-size:12px;letter-spacing:3px}
.fnav{left:408px;top:3440px;display:flex;gap:30px;font-size:14px;color:var(--white)}
.social{top:3430px;width:40px;height:40px;border-radius:50%;background:#4a4a4d}
.frule{left:90px;top:3586px;width:1020px;height:1px;background:#555}
.copy{left:0;width:1200px;top:3608px;text-align:center;font-size:12px;color:var(--white)}
.totop{left:1134px;top:3566px;width:42px;height:42px;border-radius:50%;background:var(--teal)}
</style>
</head>
<body>

<div class="abs hero-bg"></div>
<div class="abs nav-mark"></div>
<div class="abs logo">
  <div class="logo-name">RISING PATHS</div>
  <div class="logo-sub">COACHING</div>
</div>
<nav class="abs nav">
  <span class="active">HOME</span><span>ABOUT ME</span><span>SERVICES</span><span>BOGS</span><span>CONTACT US</span>
</nav>

<h1 class="abs serif hero-title">LIFE<br>COACHING<br>SERVICE</h1>
<p class="abs hero-text">Lorem Ipsum is simply dummy text of the printing and dummy typesetting industry lorem Ipsum has been elit.</p>
<div class="abs btn hero-btn">Schedule Now</div>
<div class="abs hero-leaf" role="img" aria-label="Teal leaf sprig decoration"></div>
<div class="abs hero-photo" role="img" aria-label="Head shot of the coach smiling in a kitchen"></div>

<div class="abs about-rule"></div>
<h2 class="abs serif about-title">ABOUT<br>ME</h2>
<p class="abs about-text">Lorem Ipsum is simply dummy text of the printing and typesetting industry. Lorem Ipsum has been the industry's standard dummy text ever since the 1500s, when an unknown printer took a galley of type and scrambled it to make a type specimen book. It has survived not only five centuries, but also the leap into electronic typesetting, remaining essentially unchanged. It was popularised in the 1960s with the release of Letraset sheets containing...</p>
<span class="abs link about-link">Find out more</span>

<div class="abs services-card"></div>
<div class="abs services-photo" role="img" aria-label="Couple selfie above a city skyline"></div>
<h2 class="abs serif services-title">LIFE<br>COACHING<br>SERVICES</h2>
<p class="abs services-text">Lorem Ipsum is simply dummy text of the printing and typesetting industry. Lorem Ipsum has been the industry's standard dummy text ever since the 1500s, when an unknown printer took a galley of type and scrambled it to make a type specimen book. It has survived not only five centuries, but also the leap into electronic...</p>
<span class="abs link services-link">View Services</span>

<div class="abs blogs-band"></div>
<h2 class="abs serif section-title blogs-title">OUR BLOGS</h2>
<article class="abs blog" style="left:170px">
  <div class="blog-img" role="img" aria-label="Portrait of a thoughtful woman" style="background:linear-gradient(150deg,#5a4a3c,#c08a5e 55%,#2b2624)"></div>
  <div class="blog-body"><div class="blog-date">25-02-2022</div><div class="blog-head">Some blog heading...</div><div class="blog-text">Duis sed odio sit amet nibh curus vulputate cursus a sit mauris odio morbi accumsan ipsum...</div></div>
</article>
<article class="abs blog" style="left:462px">
  <div class="blog-img" role="img" aria-label="Fountain pen writing on paper" style="background:linear-gradient(150deg,#cfcac2,#e9e6e1 50%,#9d978e)"></div>
  <div class="blog-body"><div class="blog-date">25-02-2022</div><div class="blog-head">Some blog heading...</div><div class="blog-text">Duis sed odio sit amet nibh curus vulputate cursus a sit mauris odio morbi accumsan ipsum...</div></div>
</article>
<article class="abs blog" style="left:757px">
  <div class="blog-img" role="img" aria-label="People talking across a wooden table" style="background:linear-gradient(150deg,#8a96a3,#4f5660 50%,#5a3b26)"></div>
  <div class="blog-body"><div class="blog-date">25-02-2023</div><div class="blog-head">Some blog heading...</div><div class="blog-text">Duis sed odio sit amet nibh curus vulputate cursus a sit mauris odio morbi accumsan ipsum...</div></div>
</article>

<h2 class="abs serif section-title testi-title">TESTIMONIALS</h2>
<div class="abs testi" style="left:0;width:271px">
  <div class="abs quote-mark" style="left:-10px;top:4px">&ldquo;</div>
  <p class="abs testi-text" style="left:0;top:76px;width:260px">mmy text of the printing and<br>m Ipsum has been the industry's<br>r since the 1500s...</p>
  <div class="abs testi-co" style="left:4px;top:160px">NORVALE</div>
</div>
<div class="abs testi" style="left:297px;width:606px">
  <div class="abs quote-mark" style="left:315px;top:4px">&ldquo;</div>
  <div class="abs avatar" style="left:53px;top:60px" role="img" aria-label="Client portrait"></div>
  <p class="abs testi-text" style="left:166px;top:78px;width:410px">Lorem Ipsum is simply dummy text of the printing and typesetting industry. Lorem Ipsum has been the industry's standard dummy text ever since the 1500s...</p>
  <div class="abs testi-name" style="left:169px;top:156px">Marcus Delane<span>NORVALE</span></div>
  <div class="abs testi-co" style="left:169px;top:178px">BRIGHTLANE</div>
</div>
<div class="abs testi" style="left:929px;width:300px">
  <div class="abs avatar" style="left:53px;top:60px" role="img" aria-label="Client portrait"></div>
  <p class="abs testi-text" style="left:166px;top:78px;width:300px;white-space:nowrap">Lorem Ipsum is simply<br>typesetting industry<br>standard dummy</p>
  <div class="abs testi-name" style="left:169px;top:156px">Oliver Brandt<span>NORVALE</span></div>
  <div class="abs testi-co" style="left:169px;top:178px">BRIGHTLANE</div>
</div>

<div class="abs badge" style="left:313px"><div class="badge-shape" style="width:76px;height:76px;background:#2b5676;border-radius:4px"></div></div>
<div class="abs badge" style="left:517px"><div class="badge-shape" style="width:80px;height:80px;border-radius:50%;border:6px solid #1a8fd0;background:var(--white)"></div></div>
<div class="abs badge" style="left:710px"><div class="badge-shape" style="width:76px;height:76px;background:#1f4e79;border-radius:4px"></div></div>

<footer class="abs footer"></footer>
<section class="abs cta">
  <h2 class="abs cta-title">EASY SCHEDULING<br>POSSIBILITIES AHEAD</h2>
  <div class="abs btn cta-btn">Schedule Now</div>
</section>
<div class="abs flogo">
  <div class="flogo-name">RISING PATHS</div>
  <div class="flogo-sub">COACHING</div>
</div>
<nav class="abs fnav"><span>Home</span><span>About Me</span><span>Our Services</span><span>Writing/Bogs</span><span>Contact Us</span></nav>
<div class="abs social" style="left:975px" aria-label="Social link"></div>
<div class="abs social" style="left:1023px" aria-label="Social link"></div>
<div class="abs social" style="left:1071px" aria-label="Social link"></div>
<div class="abs frule"></div>
<div class="abs copy">© Copyright 2022 All Rights Reserved</div>
<div class="abs totop">
  <svg width="42" height="42" viewBox="0 0 42 42" fill="none" stroke="#fff" stroke-width="1.6"><path d="M21 28V14M15 20l6-6 6 6"/></svg>
</div>

</body>
</html>
```